GLP letterhead

We need a letterhead design for our new company based in Los Angeles called "Gold Ladder Pictures". We develop film and television projects. We work with investors, financiers, film production companies, film distribution and sales companies as well as studios. We would like to incorporate our logo (see attached) but make the letterhead simple and elegant. We need to include: logo, company address, phone number and company website.
Updates

Hello designers, Thanks for your submissions. For our letterhead, we are looking for something more simple and elegant. No heavy bars or lines. Make it feel light and clean. Not a lot of ink on the page. Use the logo and contact info but think "clean", "streamlined" and mostly white paper. Looking forward to seeing more... thanks! Gold Ladder Pictures team

Target Market(s)

Studio executives, talent agents and agencies, financiers, investors.

Industry/Entity Type

It Company

Requirements
Must have
• Gold Ladder Pictures logo (see attached). Logo may be cropped and altered appropriately for elegant letterhead design.
• Please include:
• COMPANY ADDRESS:
• TQV Media Campus
• 2750 Halvering Avenue
• Norwick Center, 4th Floor
• Farrowdale Cove, CA 90999
• COMPANY WEBSITE:
• www.goldladderpicturesgroup.example
• COMPANY PHONE NUMBER:
• 555-014-2236

```html
<!DOCTYPE html>
<html lang="en">
<head>
<meta charset="utf-8">
<title>Gold Ladder Pictures – Letterhead</title>
<link rel="stylesheet" href="https://fonts.googleapis.com/css2?family=Michroma&family=Source+Sans+3:wght@400&display=swap">
<style>
  :root {
    --backdrop: #e9e9e9;
    --paper: #ffffff;
    --paper-shade: #f6f6f6;
    --brand-blue: #1a8fc0;
    --mark-dark: #0b1a22;
    --tagline-grey: #b9b9b9;
    --text-grey: #555a5e;
    --icon-blue: #3a7fb5;
    --watermark: #ececec;
    --band-cyan: #00b7ee;
    --band-deep: #0a6a98;
    --edge-margin: 28px;
  }
  * { margin: 0; padding: 0; box-sizing: border-box; }
  html, body {
    width: 950px; height: 1200px; overflow: hidden;
    background: var(--backdrop);
  }
  .sheet {
    position: absolute; left: 50px; top: 50px;
    width: 850px; height: 1100px;
    background: linear-gradient(180deg, var(--paper) 0%, var(--paper) 60%, var(--paper-shade) 100%);
    box-shadow: 0 1px 4px rgba(0,0,0,0.15);
  }
  .brand {
    position: absolute; left: 0; top: 30px; width: 100%;
    text-align: center;
  }
  .brand-dot {
    display: block; margin: 0 auto;
    width: 130px; height: 130px; border-radius: 50%;
    background: var(--mark-dark);
  }
  .brand-name {
    font-family: "Michroma", sans-serif;
    color: var(--brand-blue);
    font-weight: 400;
    line-height: 1;
  }
  .brand-name.primary { margin-top: 14px; font-size: 17px; letter-spacing: 1px; }
  .brand-name.secondary { margin-top: 6px; font-size: 11px; letter-spacing: 9px; padding-left: 9px; }
  .tagline {
    margin-top: 8px;
    font-family: "Source Sans 3", sans-serif;
    font-size: 7.5px; letter-spacing: 3.2px;
    color: var(--tagline-grey);
  }
  .watermark {
    position: absolute; left: 265px; top: 383px;
    width: 314px; height: 314px; border-radius: 50%;
    background: var(--watermark);
  }
  .contact, .address {
    position: absolute; top: 1029px;
    font-family: "Source Sans 3", sans-serif;
    font-size: 14.5px; line-height: 20px;
    color: var(--text-grey);
    white-space: nowrap;
  }
  .contact { left: var(--edge-margin); }
  .contact-line { display: flex; align-items: center; gap: 5px; }
  .contact-line svg { width: 13px; height: 13px; }
  .address { right: var(--edge-margin); font-style: normal; text-align: left; }
  .footer-band {
    position: absolute; left: 0; top: 1080px;
    width: 850px; height: 20px;
  }
</style>
</head>
<body>
  <main class="sheet">
    <header class="brand">
      <span class="brand-dot" aria-hidden="true"></span>
      <div class="brand-name primary">GOLD LADDER</div>
      <div class="brand-name secondary">PICTURES</div>
      <div class="tagline">A MEDIA ENTERTAINMENT COMPANY</div>
    </header>

    <div class="watermark" aria-hidden="true"></div>

    <footer>
      <div class="contact">
        <div class="contact-line">
          <svg viewBox="0 0 14 14" aria-hidden="true">
            <circle cx="7" cy="7" r="6.2" fill="none" stroke="var(--icon-blue)" stroke-width="1"/>
            <path d="M5 3.6c-.8.5-1.2 1.4-.9 2.6.5 1.8 1.9 3.5 3.6 4.2.9.3 1.7 0 2.2-.6l-1.3-1.2-.8.5c-.9-.5-1.6-1.3-2-2.3l.7-.6L5 3.6z" fill="var(--icon-blue)"/>
          </svg>
          <span>555-014-2236</span>
        </div>
        <div class="contact-line">
          <svg viewBox="0 0 14 14" aria-hidden="true">
            <g fill="none" stroke="var(--icon-blue)" stroke-width="0.9">
              <circle cx="7" cy="7" r="6.2"/>
              <ellipse cx="7" cy="7" rx="2.8" ry="6.2"/>
              <line x1="0.8" y1="7" x2="13.2" y2="7"/>
              <path d="M2 3.8h10M2 10.2h10"/>
            </g>
          </svg>
          <span>www.goldladderpicturesgroup.example</span>
        </div>
      </div>

      <address class="address">
        TQV Media Campus 2750 Halvering Avenue Norwick Center,<br>
        4th Floor Farrowdale Cove, CA 90999
      </address>

      <svg class="footer-band" viewBox="0 0 850 20" preserveAspectRatio="none" aria-hidden="true">
        <defs>
          <linearGradient id="band-fade" x1="0" y1="0" x2="1" y2="0">
            <stop offset="0" stop-color="var(--band-cyan)"/>
            <stop offset="1" stop-color="var(--band-deep)"/>
          </linearGradient>
        </defs>
        <polygon points="0,0 450,0 430,20 0,20" fill="var(--band-cyan)"/>
        <polygon points="460,0 850,0 850,20 440,20" fill="url(#band-fade)"/>
      </svg>
    </footer>
  </main>
</body>
</html>
```